Relaxation CD Cover

The relaxation cd is unique in that it does not include the typical windchimes, waterfalls, harps, etc. The feel is a mixture of jazz, spanish guitar, spiritual vibes and even some djembe drums. It includes mindfulness techniques that are used in yoga, meditation, and relaxation settings. The title right now is Gentle, Flowing Stillness. The cover should convey calm and cool with a bohemian and somewhat sultry feel. Maybe a bit afrocentric but not too much. A mock-up is attached, which includes a pic of the doctor who created the CD but the pic might be too sexy for the professional role. The color scheme especially the blue in the necklace is part of the branding so necessary to carry out. CD front and back should be consistent. Polish, modern, and clean can coexist with bohemian and relaxed. If you can do this then you've got the job! Please see both pics attached. The headshot is the desired pic to be included if artist does decide to use it but please do not feel limited to using the pics.
Updates

The pic does not have to be used in the pic...less literal please.

Target Market(s)

This CD will not only be marketed via Disc Sprout and Tunevale but also wellness stores, doc's offices;yoga retreats; local afrocentric fairs

Industry/Entity Type

Doctor

Requirements
Must have
• The color of the necklace or emphasize the necklace
Welcoming and relaxed feel (must be clear that this is a relaxation CD)
front and back must be consistent
A clear area where song titles will be located
Nice to have
• If the pic is included it should relate to the overall feel or color scheme...
Should not have
• -Bohemian does not mean messy or overly themed, e.g., too spanish or afrocentric

```html
<!DOCTYPE html>
<html lang="en">
<head>
<meta charset="utf-8">
<title>Gentle, Flowing Stillness – CD Cover</title>
<link rel="stylesheet" href="https://fonts.googleapis.com/css2?family=Cormorant+Garamond:wght@500;600&family=Open+Sans:wght@400&family=Didact+Gothic&display=swap">
<style>
  :root {
    --page: #ffffff;
    --night: #0b1a20;
    --night-soft: #10262c;
    --teal-photo: #2fae9c;
    --aqua: #3dc3c0;
    --aqua-light: #63d6cf;
    --aqua-deep: #29a9b0;
    --brand-blue: #2a83b5;
    --brand-blue-deep: #1f6f9f;
    --white: #ffffff;
    --label: #222222;
  }
  html, body {
    margin: 0;
    padding: 0;
    width: 1200px;
    height: 900px;
    overflow: hidden;
    background: var(--page);
  }
  .canvas {
    position: relative;
    width: 1200px;
    height: 900px;
    background: var(--page);
  }
  .cover {
    position: absolute;
    overflow: hidden;
    box-shadow: 2px 3px 6px rgba(0, 0, 0, 0.35);
  }
  .cover--front { left: 50px; top: 121px; width: 629px; height: 629px; }
  .cover--back { left: 709px; top: 210px; width: 451px; height: 451px; }

  .cover__photo {
    position: absolute;
    left: 0; top: 0; width: 100%;
    background:
      radial-gradient(ellipse 55% 40% at 50% 52%, rgba(47, 174, 156, 0.85), rgba(47, 174, 156, 0) 70%),
      linear-gradient(180deg, var(--night) 0%, var(--night-soft) 60%, var(--night) 100%);
  }
  .cover--front .cover__photo { height: 370px; }
  .cover--back .cover__photo { height: 294px; }

  .band { position: absolute; left: 0; width: 100%; }
  .band--aqua {
    background: linear-gradient(90deg, var(--aqua-deep) 0%, var(--aqua) 50%, var(--aqua-deep) 100%);
  }
  .band--aqua-light {
    background: linear-gradient(90deg, var(--aqua) 0%, var(--aqua-light) 45%, var(--aqua) 100%);
  }
  .band--blue {
    background: linear-gradient(90deg, var(--brand-blue-deep) 0%, var(--brand-blue) 50%, var(--brand-blue-deep) 100%);
  }
  .cover--front .band--aqua { top: 370px; height: 121px; }
  .cover--front .band--aqua-light { top: 491px; height: 98px; }
  .cover--front .band--blue { top: 589px; height: 40px; }
  .cover--back .band--aqua { top: 294px; height: 50px; }
  .cover--back .band--aqua-light { top: 344px; height: 72px; }
  .cover--back .band--blue { top: 416px; height: 35px; }

  .cover__artist {
    position: absolute;
    right: 26px;
    top: 20px;
    margin: 0;
    font-family: "Open Sans", sans-serif;
    font-weight: 400;
    font-size: 21px;
    letter-spacing: 0.5px;
    color: var(--white);
  }
  .cover__title {
    position: absolute;
    left: 0; top: 0;
    margin: 0;
    font-family: "Cormorant Garamond", serif;
    font-weight: 600;
    font-size: 64px;
    line-height: 1;
    color: var(--white);
  }
  .cover__title span { position: absolute; white-space: nowrap; }
  .title-line--1 { left: 25px; top: 389px; }
  .title-line--2 { left: 50px; top: 437px; }
  .title-line--3 { left: 100px; top: 487px; }

  .tracklist-bar {
    position: absolute;
    left: 0;
    top: 44px;
    width: 100%;
    height: 34px;
    background: rgba(61, 195, 192, 0.35);
  }
  .tracklist-bar__label {
    position: absolute;
    left: 10px;
    top: 6px;
    margin: 0;
    font-family: "Open Sans", sans-serif;
    font-size: 18px;
    color: var(--white);
  }

  .caption {
    position: absolute;
    margin: 0;
    font-family: "Didact Gothic", sans-serif;
    font-size: 24px;
    color: var(--label);
    transform: translateX(-50%);
    white-space: nowrap;
  }
  .caption--front { left: 292px; top: 788px; }
  .caption--back { left: 921px; top: 718px; }
</style>
</head>
<body>
<main class="canvas">
  <section class="cover cover--front">
    <div class="cover__photo" role="img" aria-label="Teal-toned photo of two hands joined in a meditation mudra holding a small flower, on a dark background"></div>
    <div class="band band--aqua"></div>
    <div class="band band--aqua-light"></div>
    <div class="band band--blue"></div>
    <p class="cover__artist">DR. SELENE MARLOWE</p>
    <h1 class="cover__title">
      <span class="title-line--1">Gentle,</span>
      <span class="title-line--2">Flowing</span>
      <span class="title-line--3">Stillness</span>
    </h1>
  </section>

  <section class="cover cover--back">
    <div class="cover__photo" role="img" aria-label="Teal-toned photo of two hands joined in a meditation mudra holding a small flower, on a dark background"></div>
    <div class="tracklist-bar">
      <p class="tracklist-bar__label">Tracklisting:</p>
    </div>
    <div class="band band--aqua"></div>
    <div class="band band--aqua-light"></div>
    <div class="band band--blue"></div>
  </section>

  <p class="caption caption--front">CD Cover Front</p>
  <p class="caption caption--back">CD Cover Back</p>
</main>
</body>
</html>
```